Coffeeshop menu for filter tip

We want to have a cannabis (coffeeshop) menu in the size 25mm wide x 60mm wide. Some examples attached.

it must have the following text:
Menu

WEED p/g
Velotrine €16
Cinderfox €14
Tide Rambler €14
Marigolden €16
Grand Pelican €14
Copper Comet €14

HASH p/g
Baltic Ember €12
Harbor Velvet€11
Plum Rova €14
Dusk Maple €10

Target Market(s)

tourist in Amsterdam

Requirements
Nice to have
• cannabis sign leaf
• No Cigarettes allowed symbol

```html
<!DOCTYPE html>
<html lang="en">
<head>
<meta charset="utf-8">
<title>Coffeeshop Menu</title>
<link href="https://fonts.googleapis.com/css2?family=Germania+One&family=Raleway:wght@700&display=swap" rel="stylesheet">
<style>
  :root {
    --backdrop: #606060;
    --leaf-green: #7cb83f;
    --leaf-green-soft: #86c04a;
    --leaf-green-deep: #6fae36;
    --paper: #ffffff;
    --fringe-tint: #e9f3de;
    --ink-light: #ffffff;
    --stop-red: #e0252b;
    --icon-dark: #1d1d1b;
  }
  * { margin: 0; padding: 0; box-sizing: border-box; }
  html, body {
    width: 686px; height: 1200px; overflow: hidden;
    background: var(--backdrop);
  }
  .menu-card {
    position: absolute; left: 136px; top: 100px;
    width: 419px; height: 1000px;
    background: var(--leaf-green);
    overflow: hidden;
  }
  .leaf-pattern {
    position: absolute; inset: 0;
    background:
      radial-gradient(circle at 20% 30%, var(--leaf-green-soft) 0, transparent 18%),
      radial-gradient(circle at 75% 45%, var(--leaf-green-deep) 0, transparent 16%),
      radial-gradient(circle at 30% 70%, var(--leaf-green-deep) 0, transparent 17%),
      radial-gradient(circle at 80% 85%, var(--leaf-green-soft) 0, transparent 15%),
      var(--leaf-green);
  }
  .leaf-fringe {
    position: absolute; left: 0; width: 100%;
  }
  .leaf-fringe--top {
    top: 52px; height: 34px;
    background: linear-gradient(to bottom, var(--leaf-green) 0%, var(--fringe-tint) 55%, var(--paper) 100%);
  }
  .leaf-fringe--bottom {
    top: 244px; height: 28px;
    background: linear-gradient(to bottom, var(--paper) 0%, var(--fringe-tint) 45%, var(--leaf-green) 100%);
  }
  .title-band {
    position: absolute; left: 0; top: 86px;
    width: 100%; height: 158px;
    background: var(--paper);
    display: flex; align-items: center; justify-content: center;
  }
  .menu-title {
    font-family: "Germania One", serif;
    font-size: 124px; line-height: 1;
    color: var(--leaf-green);
    letter-spacing: 2px;
    font-weight: 400;
    margin-top: 6px;
  }
  .menu-section {
    position: absolute; left: 66px; width: 308px;
    color: var(--ink-light);
  }
  .menu-section--weed { top: 284px; }
  .menu-section--hash { top: 638px; }
  .section-head {
    display: flex; justify-content: space-between; align-items: flex-end;
    height: 66px;
    padding: 0 12px 10px 4px;
    border-bottom: 2px solid var(--ink-light);
  }
  .section-title {
    font-family: "Germania One", serif;
    font-weight: 400; font-size: 58px; line-height: 1;
    letter-spacing: 1px;
  }
  .unit-label {
    font-family: "Raleway", sans-serif;
    font-weight: 700; font-size: 17px;
    letter-spacing: 1px;
    padding-bottom: 4px;
  }
  .price-list {
    list-style: none;
    margin-top: 30px;
    padding-left: 4px;
  }
  .price-list li {
    display: grid; grid-template-columns: 236px auto;
    height: 39px;
    font-family: "Germania One", serif;
    font-weight: 400; font-size: 33px; line-height: 39px;
    letter-spacing: 0.5px;
  }
  .menu-section--hash .price-list { margin-top: 28px; }
  .menu-section--hash .price-list li { height: 41px; line-height: 41px; }
  .price .currency {
    font-family: "Raleway", sans-serif;
    font-size: 20px; font-weight: 700; margin-right: 3px;
  }
  .house-rule {
    position: absolute; left: 74px; top: 920px;
    display: flex; align-items: center; gap: 16px;
    color: var(--ink-light);
    font-family: "Raleway", sans-serif;
    font-weight: 700; font-size: 28px;
  }
</style>
</head>
<body>
  <main class="menu-card">
    <div class="leaf-pattern" role="img" aria-label="Faint repeating cannabis leaf pattern across the card background"></div>
    <div class="leaf-fringe leaf-fringe--top" role="img" aria-label="Row of white cannabis leaf silhouettes along the top of the title band"></div>
    <header class="title-band">
      <h1 class="menu-title">MENU</h1>
    </header>
    <div class="leaf-fringe leaf-fringe--bottom" role="img" aria-label="Row of white cannabis leaf silhouettes along the bottom of the title band"></div>

    <section class="menu-section menu-section--weed">
      <div class="section-head">
        <h2 class="section-title">WEED</h2>
        <span class="unit-label">P/G</span>
      </div>
      <ul class="price-list">
        <li><span>Velotrine</span><span class="price"><span class="currency">€</span>16</span></li>
        <li><span>Cinderfox</span><span class="price"><span class="currency">€</span>14</span></li>
        <li><span>Tide Rambler</span><span class="price"><span class="currency">€</span>14</span></li>
        <li><span>Marigolden</span><span class="price"><span class="currency">€</span>16</span></li>
        <li><span>Grand Pelican</span><span class="price"><span class="currency">€</span>14</span></li>
        <li><span>Copper Comet</span><span class="price"><span class="currency">€</span>14</span></li>
      </ul>
    </section>

    <section class="menu-section menu-section--hash">
      <div class="section-head">
        <h2 class="section-title">HASH</h2>
        <span class="unit-label">P/G</span>
      </div>
      <ul class="price-list">
        <li><span>Baltic Ember</span><span class="price"><span class="currency">€</span>12</span></li>
        <li><span>Harbor Velvet</span><span class="price"><span class="currency">€</span>11</span></li>
        <li><span>Plum Rova</span><span class="price"><span class="currency">€</span>14</span></li>
        <li><span>Dusk Maple</span><span class="price"><span class="currency">€</span>10</span></li>
      </ul>
    </section>

    <footer class="house-rule">
      <svg class="no-smoking-icon" width="58" height="58" viewBox="0 0 58 58" aria-hidden="true">
        <circle cx="29" cy="29" r="27" fill="var(--paper)"/>
        <rect x="12" y="32" width="28" height="7" fill="var(--icon-dark)"/>
        <rect x="41" y="32" width="4" height="7" fill="var(--icon-dark)"/>
        <path d="M42 29 C38 24 44 20 40 14 M46 29 C42 24 48 20 44 14" stroke="var(--icon-dark)" stroke-width="2" fill="none"/>
        <circle cx="29" cy="29" r="25" fill="none" stroke="var(--stop-red)" stroke-width="5"/>
        <line x1="12" y1="12" x2="46" y2="46" stroke="var(--stop-red)" stroke-width="5"/>
      </svg>
      <span>No Cigarettes</span>
    </footer>
  </main>
</body>
</html>
```